Health Benefits Association Website Design

The Unified Household Wellspring Alliance (UHWA) is an organization formed for the purpose of providing its members better value for selected health benefits and services. Members can use the association benefits either in conjunction with or independently of other medical insurance they may have. Some of the benefits available include discounted dental and vision care and prescription mail order services. There is no limitation on who can join. This membership will be primarily marketed as a way to enhance the value of a fixed benefit health insurance plan although members do not have to have the insurance plan join the association.

We are seeking a design for a website to be used for consumers to get information about membership and for current members to be able to access their benefits. The website should include:

1) A landing page to provide a description of the UHWA

2) A secondary page that can be duplicated that will:
a. Provide a list of benefits
b. Provide a membership enrollment form
c. Provide a member’s only access page
d. Provide a contact page for more information

We are seeking a modern but conservative design that will reflect value, simplicity and good health. The site design will also need to be compatible for use with mobile phones and tablets.

A copy of the association logo is included with the submission. It will also need to be incorporated into the website design. Layouts of similar association websites have also been included for reference.

Target Market(s)

Ages 25 to 65 unmarried, married with no children, professionals, self-employed, active and healthy

Industry/Entity Type

Health And Wellness

Number of Pages Required

2 page

Font styles to use
Sans Serif

Colors

Designer to choose colors to be used in the design.

Requirements
Must have
• UHWA Logo (attached). Use colors from the logo in the website design.
Nice to have
• Graphics, if used, should convey health and fitness and skew toward a diverse array of adults 25 to 40.

```html
<!DOCTYPE html>
<html lang="en">
<head>
<meta charset="utf-8">
<title>Unified Household Wellspring Alliance</title>
<link rel="stylesheet" href="https://fonts.googleapis.com/css2?family=Cinzel:wght@400;700&family=Raleway:wght@400;500;600&display=swap">
<style>
:root{
  --green:#8ea53a;
  --green-dark:#6e8a1e;
  --green-light:#b7c878;
  --gold:#fcc100;
  --gold-dark:#d9a600;
  --text:#5c6a2c;
  --white:#ffffff;
  --body-text:#6b6b5a;
}
*{box-sizing:border-box;margin:0;padding:0}
html,body{width:1200px;height:4018px;overflow:hidden;background:var(--white)}
body{font-family:'Raleway',sans-serif;color:var(--body-text);position:relative}
.serif{font-family:'Cinzel',serif}
section,header,footer{position:absolute;left:0;width:1200px}

.topbar{top:0;height:43px;background:var(--green);color:var(--white);font-size:15px}
.topbar .mail{position:absolute;left:80px;top:12px;display:flex;gap:10px;align-items:center}
.topbar .call{position:absolute;right:80px;top:12px;display:flex;gap:10px;align-items:center}

.nav{top:43px;height:91px;background:var(--white)}
.nav a{position:absolute;top:37px;font-size:16px;font-weight:600;color:#555;text-decoration:none;letter-spacing:.5px}
.nav .active{left:80px;top:22px;width:92px;height:48px;background:var(--gold);color:var(--white);display:flex;align-items:center;justify-content:center;border-bottom:4px solid var(--gold-dark)}
.logo{position:absolute;left:534px;top:-36px;width:132px;height:126px;background:var(--white);border-radius:8px;display:flex;flex-direction:column;align-items:center;justify-content:center;gap:4px}
.logo .dot{width:18px;height:18px;border-radius:50%;background:var(--green)}
.logo span{font-family:'Cinzel',serif;font-weight:700;color:var(--green-dark);font-size:15px;line-height:1.05;text-align:center}
.join{position:absolute;left:978px;top:16px;width:142px;height:58px;background:var(--gold);color:var(--white);font-family:'Cinzel',serif;font-size:22px;display:flex;align-items:center;justify-content:center;border-bottom:4px solid var(--gold-dark)}

.hero{top:134px;height:482px}
.hero .photo{position:absolute;inset:0;background:linear-gradient(100deg,#9aa6b0 0%,#d9d3c4 35%,#eeeae0 60%,#f4f1ea 100%)}
.form{position:absolute;left:705px;top:26px;width:415px;height:424px;background:rgba(255,255,255,.9);border:2px solid #e7e2c4;border-radius:10px;padding:20px 22px}
.form h2{font-family:'Cinzel',serif;color:var(--green-dark);font-size:32px;line-height:1.1;text-align:center;font-weight:400;margin-bottom:20px}
.form .field{height:46px;border:2px solid #f0e6a8;background:var(--white);margin-bottom:8px;padding:0 14px;font-size:13px;color:#999;display:flex;align-items:center}
.form .submit{margin:20px auto 0;width:168px;height:62px;background:var(--gold);color:var(--white);font-family:'Cinzel',serif;font-size:22px;display:flex;align-items:center;justify-content:center;border-bottom:4px solid var(--gold-dark)}

.strip{top:616px;height:62px;background:linear-gradient(90deg,#e5ebcc,#8ea53a 35%,#8ea53a 65%,#e5ebcc);display:flex;align-items:center;justify-content:center;color:var(--white);font-family:'Cinzel',serif;font-size:22px;gap:60px}

.divider{display:flex;align-items:center;justify-content:center;gap:10px}
.divider i{display:block;width:70px;height:3px;background:var(--green-light)}
.divider b{display:block;width:20px;height:20px;border-radius:50%;background:#f7d94a}

.welcome{top:678px;height:474px;text-align:center}
.welcome h1{margin-top:112px;font-family:'Cinzel',serif;font-weight:400;font-size:52px;color:var(--green-dark);line-height:1}
.welcome .sub{font-family:'Cinzel',serif;font-size:24px;color:var(--green-light);margin:6px 0}
.welcome p{width:990px;margin:26px auto 0;font-size:14.5px;line-height:2;color:#666}

.btn{width:186px;height:60px;background:var(--gold);color:var(--white);font-family:'Cinzel',serif;font-size:22px;display:flex;align-items:center;justify-content:center;border-bottom:5px solid var(--gold-dark)}
.welcome .btn{margin:20px auto 0}

.feature{height:397px}
.feature.green{background:linear-gradient(90deg,#9fb24a 0%,#a7b957 55%,#c4d08f 100%)}
.feature .photo{position:absolute;top:60px;width:276px;height:276px;border-radius:50%;border:4px solid var(--gold);background:radial-gradient(circle at 45% 40%,#efe6da,#b8b1a5)}
.feature.green .photo{left:126px}
.feature.white .photo{left:840px;border-color:#9aaa6a}
.feature .body{position:absolute;top:96px;width:645px}
.feature.green .body{left:477px;color:var(--white)}
.feature.white .body{left:80px}
.feature h3{font-family:'Cinzel',serif;font-weight:400;font-size:36px;color:var(--white);display:flex;align-items:center;gap:12px}
.feature.white h3{color:var(--green-dark)}
.feature h3 .dot{width:20px;height:20px;border-radius:50%;background:#f7d94a}
.feature h3 .line{width:70px;height:3px;background:var(--green-light)}
.feature p{font-size:13.5px;line-height:2;margin-top:10px}
.feature .btn{margin-top:16px}

.news{top:3134px;height:542px}
.news h2{margin-top:130px;display:flex;justify-content:center;align-items:center;gap:14px;font-family:'Cinzel',serif;font-weight:400;font-size:46px;color:var(--green-dark)}
.news h2 i{display:block;width:70px;height:3px;background:var(--green-light)}
.news h2 b{display:block;width:20px;height:20px;border-radius:50%;background:#f7d94a}
.card{position:absolute;top:204px;width:332px}
.card .img{height:220px}
.card .date{position:absolute;left:0;top:193px;width:91px;height:86px;background:var(--gold);color:var(--white);text-align:center;font-family:'Cinzel',serif;line-height:1}
.card .date strong{display:block;font-size:38px;margin-top:10px}
.card .date span{font-size:16px}
.card .title{position:absolute;left:108px;top:230px;font-family:'Cinzel',serif;font-size:16px;color:var(--green-dark);font-weight:700}
.card .snip{position:absolute;left:108px;top:256px;font-size:14px;color:#666}

.footer{top:3676px;height:342px;background:var(--green);text-align:center;color:var(--white)}
.footer .brand{margin-top:40px;font-family:'Cinzel',serif;font-weight:700;font-size:22px;line-height:1.15}
.footer .social{margin-top:46px;display:flex;justify-content:center;gap:14px}
.footer .social span{width:40px;height:40px;border-radius:50%;background:var(--gold)}
.footer nav{margin-top:30px;font-size:14px;display:flex;justify-content:center;gap:22px}
.footer nav span.sep{opacity:.6}
.footer .copy{margin-top:12px;font-size:14px}
</style>
</head>
<body>

<header class="topbar">
  <div class="mail">
    <svg width="20" height="14" viewBox="0 0 20 14"><rect x="0.5" y="0.5" width="19" height="13" fill="#fcc100"/><path d="M1 1l9 7 9-7" stroke="#8ea53a" stroke-width="1.6" fill="none"/></svg>
    info@wellspringalliance.org
  </div>
  <div class="call">Call Us :
    <svg width="16" height="16" viewBox="0 0 16 16"><path d="M3 1l3 3-2 2c1 2 3 4 5 5l2-2 3 3-2 3C7 15 1 9 1 3z" fill="#fcc100"/></svg>
    555 010 2740
  </div>
</header>

<header class="nav">
  <a class="active">HOME</a>
  <a style="left:196px">ABOUT</a>
  <a style="left:276px">BENEFITS</a>
  <a style="left:372px">NEWS</a>
  <a style="left:442px">CHARITIES</a>
  <div class="logo"><div class="dot"></div><span>UNIFIED<br>HOUSEHOLD<br>WELLSPRING</span></div>
  <a style="left:675px">MEMBERSHIP</a>
  <a style="left:828px">CONTACT</a>
  <div class="join">JOIN US</div>
</header>

<section class="hero">
  <div class="photo" role="img" aria-label="Older couple walking hand in hand on a sunny beach"></div>
  <div class="form">
    <h2>Membership<br>Enrollment Form</h2>
    <div class="field">Enter Name*</div>
    <div class="field">Enter Email*</div>
    <div class="field">Enter Phone*</div>
    <div class="field">Address*</div>
    <div class="submit">SUBMIT</div>
  </div>
</section>

<section class="strip">
  <svg width="14" height="24" viewBox="0 0 14 24"><path d="M12 2L2 12l10 10" stroke="#fff" stroke-width="2" fill="none"/></svg>
  <span>The Unified Household Wellspring Alliance</span>
  <svg width="14" height="24" viewBox="0 0 14 24"><path d="M2 2l10 10-10 10" stroke="#fff" stroke-width="2" fill="none"/></svg>
</section>

<section class="welcome">
  <h1>Welcome To The Unified Household</h1>
  <div class="divider"><i></i><b></b><span class="sub">Wellspring Alliance</span><b></b><i></i></div>
  <p>Welcome to the Unified Household Wellspring Alliance (UHWA). UHWA was started to be part of a member-focused organization that is different from other groups with a similar purpose. UHWA believes a member group should focus on delivering value to support its mission, not its leaders. So, none of the UHWA officers or board members receive any compensation. Please read the description of what UHWA is about and how we go about bringing value to our members.</p>
  <div class="btn">KNOW MORE</div>
</section>

<section class="feature green" style="top:1152px">
  <div class="photo" role="img" aria-label="Smiling senior couple embracing"></div>
  <div class="body">
    <h3>Dental <span class="dot"></span><span class="line"></span></h3>
    <p>Lorem Ipsum is simply dummy text of the printing and typesetting industry. Lorem Ipsum has been the industry's standard dummy text ever since the 1500s, when an unknown.</p>
    <p>Lorem Ipsum is simply dummy text of the printing and typesetting industry. Lorem Ipsum has been the industry's standard dummy text ever since the 1500s, when an unknown.</p>
    <div class="btn">KNOW MORE</div>
  </div>
</section>

<section class="feature white" style="top:1549px">
  <div class="body">
    <h3>Vision Care <span class="dot"></span><span class="line"></span></h3>
    <p>Lorem Ipsum is simply dummy text of the printing and typesetting industry. Lorem Ipsum has been the industry's standard dummy text ever since the 1500s, when an unknown.</p>
    <p>Lorem Ipsum is simply dummy text of the printing and typesetting industry. Lorem Ipsum has been the industry's standard dummy text ever since the 1500s, when an unknown.</p>
    <div class="btn">KNOW MORE</div>
  </div>
  <div class="photo" role="img" aria-label="Smiling professional woman with a colleague in an office"></div>
</section>

<section class="feature green" style="top:1945px">
  <div class="photo" role="img" aria-label="Senior couple looking at a laptop together"></div>
  <div class="body">
    <h3>Prescription <span class="dot"></span></h3>
    <p>Lorem Ipsum is simply dummy text of the printing and typesetting industry. Lorem Ipsum has been the industry's standard dummy text ever since the 1500s, when an unknown.</p>
    <p>Lorem Ipsum is simply dummy text of the printing and typesetting industry. Lorem Ipsum has been the industry's standard dummy text ever since the 1500s, when an unknown.</p>
    <div class="btn">KNOW MORE</div>
  </div>
</section>

<section class="feature white" style="top:2342px">
  <div class="body">
    <h3>Mail Order <span class="dot"></span><span class="line"></span></h3>
    <p>Lorem Ipsum is simply dummy text of the printing and typesetting industry. Lorem Ipsum has been the industry's standard dummy text ever since the 1500s, when an unknown.</p>
    <p>Lorem Ipsum is simply dummy text of the printing and typesetting industry. Lorem Ipsum has been the industry's standard dummy text ever since the 1500s, when an unknown.</p>
    <div class="btn">KNOW MORE</div>
  </div>
  <div class="photo" role="img" aria-label="Woman working on a laptop at home"></div>
</section>

<section class="feature green" style="top:2738px">
  <div class="photo" role="img" aria-label="Senior woman reading with her partner"></div>
  <div class="body">
    <h3>About Us</h3>
    <p>Lorem Ipsum is simply dummy text of the printing and typesetting industry. Lorem Ipsum has been the industry's standard dummy text ever since the 1500s, when an unknown.</p>
    <p>Lorem Ipsum is simply dummy text of the printing and typesetting industry. Lorem Ipsum has been the industry's standard dummy text ever since the 1500s, when an unknown.</p>
    <div class="btn">KNOW MORE</div>
  </div>
</section>

<section class="news">
  <h2><i></i><b></b>Latest News<b></b><i></i></h2>
  <article class="card" style="left:78px">
    <div class="img" role="img" aria-label="Hands sheltering paper family cut-outs" style="background:linear-gradient(180deg,#d8b29a,#f2e6dc)"></div>
    <div class="date"><strong>23</strong><span>MAY</span></div>
    <div class="title">Lorem Ipsum is simply</div>
    <div class="snip">Lorem Ipsum is simply</div>
  </article>
  <article class="card" style="left:434px">
    <div class="img" role="img" aria-label="Couple walking near a famous tower in a park" style="background:linear-gradient(180deg,#c9d6e2,#e9e6dc)"></div>
    <div class="date"><strong>24</strong><span>MAY</span></div>
    <div class="title">Lorem Ipsum is simply</div>
    <div class="snip">Lorem Ipsum is simply</div>
  </article>
  <article class="card" style="left:790px">
    <div class="img" role="img" aria-label="Family walking together on a beach" style="background:linear-gradient(180deg,#e4eaee,#eadfcc)"></div>
    <div class="date"><strong>25</strong><span>MAY</span></div>
    <div class="title">Lorem Ipsum is simply</div>
    <div class="snip">Lorem Ipsum is simply</div>
  </article>
</section>

<footer class="footer">
  <div class="brand">UNIFIED HOUSEHOLD<br>WELLSPRING</div>
  <div class="social"><span></span><span></span><span></span></div>
  <nav><span>Home</span><span class="sep">|</span><span>About</span><span class="sep">|</span><span>Benefits</span><span class="sep">|</span><span>News</span><span class="sep">|</span><span>Charities</span><span class="sep">|</span><span>Membership</span><span class="sep">|</span><span>Contact</span></nav>
  <div class="copy">© The Unified Household Wellspring Alliance (UHWA) - 2017. All rights reserved.</div>
</footer>

</body>
</html>
```